Maple Glow Label

Design a label for new brand called Maple Glow. The specific product label :
Maple Glow Cocoa Butter Lotion. You only need to design the front label.
I have included the logo and a bottle jpeg with 2 bottles on it. Please try your best.

Requirements
Must have
• text on the label other than the logo:
cocoa butter
lotion
8.5oz/250ml

Original Moisturizing Formula
Smoothes Marks
Protect Skin

__________________________________
- ALTERNATIVE TEXT TO ALSO USE:
Smoothes Dry Skin, Blemishes & Stretch Marks
Softens Hands, Face and Body
Vitamin E

```html
<!DOCTYPE html>
<html lang="en">
<head>
<meta charset="UTF-8">
<title>Maple Glow Cocoa Butter Lotion – Front Label</title>
<link rel="stylesheet" href="https://fonts.googleapis.com/css2?family=Lato:wght@400;700;900&display=swap">
<style>
  :root {
    --label-cream: #efe6d1;
    --pattern-light: #f3ecdc;
    --pattern-tone: #e6d9bb;
    --band-purple: #3c2a5b;
    --band-text: #f3eee6;
    --brand-pink: #e0197d;
    --type-dark: #3a2550;
    --size-grey: #4a4a4a;
  }
  * { margin: 0; padding: 0; box-sizing: border-box; }
  html, body {
    width: 1200px;
    height: 2452px;
    overflow: hidden;
    background: var(--label-cream);
  }
  .label {
    position: relative;
    width: 1200px;
    height: 2452px;
    font-family: "Lato", Arial, sans-serif;
    overflow: hidden;
  }
  .label__pattern {
    position: absolute;
    inset: 0;
    background: linear-gradient(160deg, var(--pattern-light) 0%, var(--label-cream) 50%, var(--pattern-tone) 100%);
  }
  .band {
    position: absolute;
    left: 0;
    width: 100%;
    background: var(--band-purple);
    color: var(--band-text);
  }
  .band--top {
    top: 300px;
    height: 170px;
    display: flex;
    align-items: center;
    justify-content: center;
  }
  .band__vitamin {
    font-size: 64px;
    font-weight: 400;
  }
  .band--claims {
    top: 1560px;
    height: 400px;
    display: flex;
    align-items: center;
    padding-left: 110px;
  }
  .claims li {
    list-style: none;
    font-size: 62px;
    line-height: 88px;
    font-weight: 400;
  }
  .brand {
    position: absolute;
    top: 920px;
    left: 0;
    width: 100%;
    display: flex;
    justify-content: center;
  }
  .brand__lockup {
    display: inline-flex;
    flex-direction: column;
    align-items: flex-end;
  }
  .brand__name {
    font-size: 190px;
    font-weight: 900;
    color: var(--brand-pink);
    letter-spacing: -2px;
    line-height: 1;
  }
  .brand__product {
    margin-top: 24px;
    font-size: 78px;
    font-weight: 700;
    color: var(--type-dark);
    line-height: 1;
  }
  .net-content {
    position: absolute;
    top: 2230px;
    left: 0;
    width: 100%;
    text-align: center;
    font-size: 58px;
    color: var(--size-grey);
  }
</style>
</head>
<body>
  <main class="label">
    <div class="label__pattern" role="img" aria-label="Soft cream paisley pattern across the label background"></div>

    <div class="band band--top">
      <span class="band__vitamin">Vitamin E</span>
    </div>

    <div class="brand">
      <div class="brand__lockup">
        <h1 class="brand__name">Maple Glow</h1>
        <p class="brand__product">cocoa butter lotion</p>
      </div>
    </div>

    <div class="band band--claims">
      <ul class="claims">
        <li>Protects Skin</li>
        <li>Smoothes Dry Skin</li>
        <li>Softens Hands, Face and Body</li>
      </ul>
    </div>

    <p class="net-content">8.5oz/250ml</p>
  </main>
</body>
</html>
```